Conveyancing Brochure

I am after a 4 page brochure for our Conveyancing division in our law firm Drovane Pitt Hollis Lawyers.

We are a diverse range of energetic, dynamic and innovative professionals who strive to be at the forefront of progressive legal service. Please refer to our website for more information: www.dphlegal-example.com.au

I would like to see the colours of our logo & also some images incorporated throughout the brochure (however I don't want it to look 'too busy' either).

The images can be based around the range of services that we provide eg: residential, development etc.

Thank you,
Mabel

```html
<!DOCTYPE html>
<html lang="en">
<head>
<meta charset="utf-8">
<title>Drovane Pitt Hollis Lawyers – Conveyancing Brochure</title>
<link rel="stylesheet" href="https://fonts.googleapis.com/css2?family=Source+Sans+3:wght@300;400;600&display=swap">
<style>
  :root {
    --ink: #3a3a3a;
    --band-dark: #1c5f80;
    --band-mid: #2b87ad;
    --band-light: #46aed3;
    --bullet: #1f86b3;
    --divider: #9cc6d8;
    --paper: #ffffff;
    --sky-top: #5f9fd6;
    --sky-bottom: #b9d6ee;
    --city: #8d8378;
    --glass-top: #1d73c8;
    --glass-bottom: #8ec4ee;
  }
  * { box-sizing: border-box; margin: 0; padding: 0; }
  html, body { width: 1200px; height: 423px; overflow: hidden; background: var(--paper); }
  body { font-family: "Source Sans 3", "Myriad Pro", Arial, sans-serif; color: var(--ink); }

  .brochure { position: relative; width: 1200px; height: 423px; background: var(--paper); }
  .panel { position: absolute; top: 0; width: 600px; height: 423px; }
  .panel--left { left: 0; }
  .panel--right { left: 600px; border-left: 1px solid var(--divider); }

  .photo { position: absolute; top: 0; left: 0; width: 100%; height: 188px; }
  .photo--city {
    background: linear-gradient(180deg, var(--sky-top) 0%, var(--sky-bottom) 45%, var(--city) 80%, #6f8f8a 100%);
  }
  .photo--tower {
    background: linear-gradient(160deg, #cfe6f7 0%, var(--glass-bottom) 30%, var(--glass-top) 70%, #2f6aa6 100%);
  }

  .brand {
    position: absolute; top: 0; left: 0; width: 172px; height: 80px;
    background: var(--paper);
    display: flex; align-items: center; gap: 8px; padding-left: 16px;
  }
  .brand__mark { width: 14px; height: 14px; background: var(--band-mid); flex: none; }
  .brand__name { font-weight: 400; color: #1d1d1d; font-size: 16px; line-height: 16px; letter-spacing: -0.3px; }
  .brand__name small { display: block; font-size: 8px; letter-spacing: 0.5px; line-height: 11px; }

  .band {
    position: absolute; height: 30px;
    background: linear-gradient(90deg, var(--band-dark) 0%, var(--band-mid) 60%, var(--band-light) 100%);
    color: #fff; font-weight: 300; font-size: 24px; line-height: 30px;
    border-radius: 0 12px 12px 0;
    box-shadow: 0 0 0 1px rgba(255,255,255,0.6);
  }
  .band--intro { top: 158px; left: 0; width: 300px; padding-left: 36px; }
  .band--services { top: 258px; left: 0; width: 160px; padding-left: 36px; }
  .band--why { top: 158px; left: 36px; width: 516px; padding-left: 38px; border-radius: 12px; }
  .band--difference { top: 274px; left: 36px; width: 520px; padding-left: 30px; border-radius: 12px; }

  .copy { position: absolute; font-size: 11.2px; line-height: 13.4px; }
  .copy--intro { top: 194px; left: 36px; width: 530px; }
  .copy--why { top: 194px; left: 36px; width: 530px; column-count: 2; column-gap: 24px; }

  .list { position: absolute; list-style: none; font-size: 11.2px; line-height: 13px; }
  .list li { position: relative; padding-left: 12px; }
  .list li::before {
    content: ""; position: absolute; left: 0; top: 5px;
    width: 4px; height: 4px; border-radius: 50%; background: var(--bullet);
  }
  .list--services-a { top: 296px; left: 36px; width: 256px; }
  .list--services-b { top: 296px; left: 311px; width: 256px; }
  .list--difference { top: 312px; left: 36px; width: 540px; }
</style>
</head>
<body>
<main class="brochure">
  <section class="panel panel--left">
    <div class="photo photo--city" role="img" aria-label="Harbour city skyline with office towers and a bridge pylon under a blue sky"></div>
    <div class="brand">
      <span class="brand__mark"></span>
      <span class="brand__name">Drovane Pitt Hollis<small>LAWYERS</small></span>
    </div>
    <h2 class="band band--intro">What is conveyancing?</h2>
    <p class="copy copy--intro">Simply put, conveyancing is the legal process in transferring title between two or more parties. There are a few steps involved between signing the contract and settlement, and you will need the right people to guide you along the way. Whether you are buying or selling, our team of experienced lawyers can help.</p>
    <h2 class="band band--services">Services:</h2>
    <ul class="list list--services-a">
      <li>Preparation of contracts</li>
      <li>Pre-contractual review of contract</li>
      <li>Advice on terms of the contract</li>
      <li>Negotiate terms with the vendor/purchaser</li>
      <li>Advise you as to various searches required and obtain searches on your behalf</li>
      <li>Communicate with your lender or broker to ensure finance is ready for settlement</li>
    </ul>
    <ul class="list list--services-b">
      <li>Attend to exchange of contracts</li>
      <li>Advise in relation to mortgage documents</li>
      <li>Preparation of transfer documents</li>
      <li>Liaising with your lender and the agent</li>
      <li>Calculation of settlement adjustments</li>
      <li>Preparing and attending settlement</li>
      <li>Communicating and keeping you updated on the progress of your matter</li>
    </ul>
  </section>

  <section class="panel panel--right">
    <div class="photo photo--tower" role="img" aria-label="Glass office building against a clear blue sky with a flag and overhanging tree leaves"></div>
    <h2 class="band band--why">Why use a lawyer and not a conveyancer?</h2>
    <p class="copy copy--why">A lawyer and conveyancer perform the same services in a simple conveyance, but you will need a lawyer if a complex legal issue arises. We can provide you with the right advice and options to ensure that the conveyance process is as smooth as possible.</p>
    <h2 class="band band--difference">The Drovane Pitt Hollis Lawyers difference</h2>
    <ul class="list list--difference">
      <li>Unlimited contracts review</li>
      <li>Fast response time</li>
      <li>Professional and reliable service</li>
      <li>One-stop-shop for all your legal, financial and accounting requirements for your sale and purchase</li>
    </ul>
  </section>
</main>
</body>
</html>
```